REDESIGN SIGN UP PAGE - EASY TO READ AND UNDERSTAND QUICKLY

I need to redesign my sign up page DESKTOP AND MOBILE VERSION to include 2 products that are each available as a monthly subscription, 6 mth or 12 mth subscription.

Currently I only promote one product on my website but now will be two. https://www.brightlanerewardhub.biz/signup

Now I will have two products:

1. UNLIMITED VACATION CERTIFICATES, DINING VOUCHERS & SAVINGS INCENTIVES
Unlimited Monthly Plan $99 / Month + $199 One-Time Set-Up Fee
Unlimited Bi Annual Plan $490 / 6 Months + $199 One-Time Set-Up Fee
Unlimited Annual Plan $898 / 12 Months + $199 One-Time Set-Up Fee

2. UNLIMITED SMART DEVICE INCENTIVES & OTHER HARD PREMIUMS
Unlimited Monthly Plan $299 / Month + $199 One-Time Set-Up Fee
Unlimited Bi Annual Plan $1,590 / 6 Months + $199 One-Time Set-Up Fee
Unlimited Annual Plan $2,898 / 12 Months + $199 One-Time Set-Up Fee

When promoting the different plans you can see the different categories of incentives I offer here: https://www.brightlanerewardhub.biz/incentives

The SMART DEVICE CERTIFICATES & INCENTIVES category is for product #2 and all the rest of the Categories is for Product #1 Feel free to use images as a visual so customers can see that this product includes Vacations & Restaurants and this product includes only smart devices....

USE ALL CURRENT BULLET POINTS FOR BOTH PLANS THAT IS CURRENTLY ON WEBSITE. USE ALL CURRENT CONTENT ON WEBSITE ORIGINAL SIGN UP PAGE. DO NOT LEAVE ANY CONTENT OUT.

Target Market(s)

BUSINESS OWNERS

Industry/Entity Type

Marketing

Number of Pages Required

2 page

Requirements
Must have
• When promoting the 2 different products on the new sign up page you can see the different categories of incentives I offer here: https://www.brightlanerewardhub.biz/incentives fee; free to use images to showcase what each product offers.

The SMART DEVICE CERTIFICATES & INCENTIVES category is for product #2 and all the rest of the Categories is for Product #1

I want the user to easily understand we have two products that are available in 3 ways, monthly subscription, bi annual and annual and can see the price immediately for all 3 options for both products without toggling, etc.

Must be super clean easy to ready design. Not too busy at all please
Nice to have
• USE ALL CURRENT BULLET POINTS FOR BOTH PLANS THAT IS CURRENTLY ON WEBSITE. USE ALL CURRENT CONTENT ON WEBSITE ORIGINAL SIGN UP PAGE. DO NOT LEAVE ANY CONTENT OUT.

Should not have

```html
<!DOCTYPE html>
<html lang="en">
<head>
<meta charset="utf-8">
<title>Sign Up – Products &amp; Plans</title>
<link href="https://fonts.googleapis.com/css2?family=Montserrat:wght@400;500;600;700;800&display=swap" rel="stylesheet">
<style>
:root{
  --ink:#111111;
  --blue:#2f7ae5;
  --blue-btn:#2a76e3;
  --orange:#ee9a2c;
  --line:#d9d9d9;
  --panel:#f5f5f5;
  --soft:#eef3fd;
  --soft-border:#c5d5f3;
  --white:#ffffff;
}
*{margin:0;padding:0;box-sizing:border-box}
html,body{width:767px;height:1200px;overflow:hidden;background:var(--white)}
body{position:relative;font-family:'Montserrat',sans-serif;color:var(--ink)}
.abs{position:absolute}
.badge{left:357px;top:58px;width:54px;height:54px;border-radius:50%;background:#0c6fc4;border:2px solid #c9d3de;display:flex;align-items:center;justify-content:center}
.headline{left:0;top:138px;width:767px;text-align:center;font-weight:800;font-size:27px;line-height:26px;letter-spacing:-.2px}
.headline .hl{color:var(--blue)}
.intro{left:0;top:242px;width:767px;text-align:center;font-size:15px;line-height:17px;font-weight:400}

.product{top:296px;width:284px;height:60px;border:1px solid var(--soft-border);border-radius:8px;background:var(--soft);display:flex;align-items:center;gap:10px;padding:0 12px}
.product .num{flex:none;width:26px;height:26px;border-radius:50%;background:var(--blue-btn);color:var(--white);font-weight:800;font-size:12px;display:flex;align-items:center;justify-content:center}
.product .kicker{font-size:7px;font-weight:700;color:var(--orange);letter-spacing:.4px;margin-bottom:3px}
.product .name{font-size:9px;font-weight:700;line-height:11px}

.plan{top:385px;width:130px;height:664px;border:1px solid var(--line);background:var(--white)}
.plan .title{position:absolute;left:0;top:8px;width:100%;text-align:center;font-weight:800;font-size:15px;line-height:13px}
.plan .title .term{color:var(--orange)}
.plan .note{position:absolute;left:0;top:56px;width:100%;text-align:center;font-size:6.6px;line-height:7px;color:var(--blue);font-weight:500}
.plan .rule{position:absolute;left:0;width:100%;height:1px;background:var(--line)}
.plan .tag{position:absolute;left:0;width:100%;text-align:center;font-size:6px;font-weight:700;letter-spacing:.3px;color:#555}
.plan .tag b{color:var(--blue)}
.plan .price{position:absolute;left:0;width:100%;text-align:center;white-space:nowrap}
.plan .price b{font-size:16px;color:var(--blue);font-weight:800;letter-spacing:-.3px}
.plan .price span{font-size:8.5px;font-weight:500}
.plan .setup{position:absolute;left:0;top:192px;width:100%;text-align:center;font-size:6.8px;font-weight:500}

.btn{position:absolute;height:17px;border-radius:5px;background:var(--blue-btn);color:var(--white);font-size:7px;font-weight:700;display:flex;align-items:center;justify-content:center;gap:4px}
.btn i{width:8px;height:8px;border-radius:50%;background:var(--white);display:inline-flex;align-items:center;justify-content:center}
.plan .btn{left:25px;width:80px}

.features{left:95px;top:593px;width:163px;height:456px;background:var(--panel)}
.feature{position:absolute;left:8px;font-size:8px;font-weight:700;line-height:7px;width:155px}
</style>
</head>
<body>

<div class="abs badge">
  <svg width="30" height="30" viewBox="0 0 30 30" fill="none" stroke="#fff" stroke-width="1.8" stroke-linejoin="round" stroke-linecap="round">
    <rect x="4" y="14" width="5" height="11"/>
    <path d="M9 15l4-6v-4c0-1 2-1 2.5 1l.5 5h6a2 2 0 0 1 0 4h-1a2 2 0 0 1 0 3h-1a2 2 0 0 1 0 3h-1.5a2 2 0 0 1 0 3H9"/>
    <path d="M15 1v2M10.5 3l1 1.5M19.5 3l-1 1.5"/>
  </svg>
</div>

<h1 class="abs headline">Congratulations on Making the<br>Decision to Make <span class="hl">More Money for</span><br><span class="hl">Your Business</span></h1>

<p class="abs intro">This program is an online subscription based incentive<br>marketing system with the following features</p>

<div class="abs product" style="left:95px">
  <div class="num">1</div>
  <div><div class="kicker">PRODUCT 1</div><div class="name">Unlimited Vacation Certificates, Dining Vouchers &amp; Savings Incentives</div></div>
</div>
<div class="abs product" style="left:397px">
  <div class="num">2</div>
  <div><div class="kicker">PRODUCT 2</div><div class="name">Unlimited Smart Device Incentives &amp; Other Hard Premiums</div></div>
</div>

<div class="abs features">
  <div class="feature" style="top:12px">Unlimited E-Certificates</div>
  <div class="feature" style="top:30px">Unlimited SMS Certificates</div>
  <div class="feature" style="top:49px">Unlimited Web Banner Certificates</div>
  <div class="feature" style="top:68px">Unlimited White Label Certificate<br>Landing Pages</div>
  <div class="feature" style="top:94px">Unlimited Website Sticky Bar<br>Certificates</div>
  <div class="feature" style="top:119px">Unlimited Website Pop Up<br>Certificate</div>
  <div class="feature" style="top:144px">Unlimited API E-Certificates</div>
  <div class="feature" style="top:163px">Unlimited LinkFlow Integration<br>Access</div>
  <div class="feature" style="top:188px">FREE Warm Lead Letter Templates</div>
  <div class="feature" style="top:206px">FREE Customer Appreciation<br>Letter Templates</div>
  <div class="feature" style="top:231px">FREE Professional-Grade Incentive<br>Videos</div>
  <div class="feature" style="top:257px">FREE Proven SocialFeed™ Ad<br>Templates</div>
  <div class="feature" style="top:282px">FREE High-Converting Banner<br>Ad Templates</div>
  <div class="feature" style="top:307px">FREE Time-Tested Print<br>Ad Templates</div>
  <div class="feature" style="top:333px">FREE White Label Redemption<br>Website</div>
  <div class="feature" style="top:358px">FREE Industry Specific Ad Packs</div>
  <div class="feature" style="top:377px">FREE Affiliate Program-Earn<br>50% Commissions</div>
  <div class="feature" style="top:401px">FREE Eye-Catching Posters,<br>Flyers &amp; Brochures Each Certificate</div>
  <div class="feature" style="top:426px">FREE Step by Step Redemption<br>Guides</div>
</div>

<section class="abs plan" style="left:273px">
  <div class="title">Unlimited<br><span class="term">Monthly</span><br>Plan</div>
  <div class="note">One Account Can be used for<br>unlimited brands</div>
  <div class="rule" style="top:76px"></div>
  <div class="tag" style="top:84px"><b>1</b> · VACATION, DINING &amp; SAVINGS</div>
  <div class="price" style="top:93px"><b>$99</b> <span>/ month</span></div>
  <div class="btn" style="top:115px">SELECT <i><svg width="6" height="6" viewBox="0 0 6 6"><path d="M1 3h4M3 1l2 2-2 2" stroke="#2a76e3" stroke-width="1.2" fill="none"/></svg></i></div>
  <div class="tag" style="top:140px"><b>2</b> · SMART DEVICES &amp; PREMIUMS</div>
  <div class="price" style="top:149px"><b>$299</b> <span>/ month</span></div>
  <div class="btn" style="top:171px">SELECT <i><svg width="6" height="6" viewBox="0 0 6 6"><path d="M1 3h4M3 1l2 2-2 2" stroke="#2a76e3" stroke-width="1.2" fill="none"/></svg></i></div>
  <div class="setup">+ $199 One-time Set-up fee</div>
  <div class="rule" style="top:207px"></div>
</section>

<section class="abs plan" style="left:412px">
  <div class="title">Unlimited<br><span class="term">Bi Annual</span><br>Plan</div>
  <div class="note">One Account Can be used for<br>unlimited brands</div>
  <div class="rule" style="top:76px"></div>
  <div class="tag" style="top:84px"><b>1</b> · VACATION, DINING &amp; SAVINGS</div>
  <div class="price" style="top:93px"><b>$490</b> <span>/ 6 months</span></div>
  <div class="btn" style="top:115px">SELECT <i><svg width="6" height="6" viewBox="0 0 6 6"><path d="M1 3h4M3 1l2 2-2 2" stroke="#2a76e3" stroke-width="1.2" fill="none"/></svg></i></div>
  <div class="tag" style="top:140px"><b>2</b> · SMART DEVICES &amp; PREMIUMS</div>
  <div class="price" style="top:149px"><b>$1,590</b> <span>/ 6 months</span></div>
  <div class="btn" style="top:171px">SELECT <i><svg width="6" height="6" viewBox="0 0 6 6"><path d="M1 3h4M3 1l2 2-2 2" stroke="#2a76e3" stroke-width="1.2" fill="none"/></svg></i></div>
  <div class="setup">+ $199 One-time Set-up fee</div>
  <div class="rule" style="top:207px"></div>
</section>

<section class="abs plan" style="left:551px">
  <div class="title">Unlimited<br><span class="term">Annual</span><br>Plan</div>
  <div class="note">One Account Can be used for<br>unlimited brands</div>
  <div class="rule" style="top:76px"></div>
  <div class="tag" style="top:84px"><b>1</b> · VACATION, DINING &amp; SAVINGS</div>
  <div class="price" style="top:93px"><b>$898</b> <span>/ 12 months</span></div>
  <div class="btn" style="top:115px">SELECT <i><svg width="6" height="6" viewBox="0 0 6 6"><path d="M1 3h4M3 1l2 2-2 2" stroke="#2a76e3" stroke-width="1.2" fill="none"/></svg></i></div>
  <div class="tag" style="top:140px"><b>2</b> · SMART DEVICES &amp; PREMIUMS</div>
  <div class="price" style="top:149px"><b>$2,898</b> <span>/ 12 months</span></div>
  <div class="btn" style="top:171px">SELECT <i><svg width="6" height="6" viewBox="0 0 6 6"><path d="M1 3h4M3 1l2 2-2 2" stroke="#2a76e3" stroke-width="1.2" fill="none"/></svg></i></div>
  <div class="setup">+ $199 One-time Set-up fee</div>
  <div class="rule" style="top:207px"></div>
</section>

<svg class="abs" style="left:0;top:593px" width="767" height="460" aria-hidden="true">
  <defs>
    <polyline id="tick" points="0,5 5,10 14,1" fill="none" stroke="#4d8ee0" stroke-width="2.6" stroke-linecap="round" stroke-linejoin="round"/>
    <g id="row"><use href="#tick" x="331"/><use href="#tick" x="470"/><use href="#tick" x="609"/></g>
  </defs>
  <use href="#row" y="11"/><use href="#row" y="29"/><use href="#row" y="48"/><use href="#row" y="67"/>
  <use href="#row" y="93"/><use href="#row" y="118"/><use href="#row" y="143"/><use href="#row" y="162"/>
  <use href="#row" y="186"/><use href="#row" y="205"/><use href="#row" y="230"/><use href="#row" y="255"/>
  <use href="#row" y="281"/><use href="#row" y="306"/><use href="#row" y="331"/><use href="#row" y="357"/>
  <use href="#row" y="376"/><use href="#row" y="401"/><use href="#row" y="425"/>
</svg>

<div class="btn" style="left:275px;top:1066px;width:61px">SELECT 1</div>
<div class="btn" style="left:340px;top:1066px;width:61px">SELECT 2</div>
<div class="btn" style="left:414px;top:1066px;width:61px">SELECT 1</div>
<div class="btn" style="left:479px;top:1066px;width:61px">SELECT 2</div>
<div class="btn" style="left:553px;top:1066px;width:61px">SELECT 1</div>
<div class="btn" style="left:618px;top:1066px;width:61px">SELECT 2</div>

</body>
</html>
```